Referral Card thats different from the rest

Business card size-

Referral card that will be given to clients, in turn they will pass it on to their friends.

The referee will add their name and address, and friends name to card before it is passed on

Referee gets 2 FREE movie tickets

Friend gets $25 OFF their service

Company is an electrical contracting company specialising in the domestic market.

I would like the card to be fun not so serious!
Completely open minded to any and every creative idea!

attached is 2 photo of an example of what another business has, i am trying to achieve something similiar
Updates

I have increased the budget, ;)

i have added 2 x photos of what i am trying to achieve. this is from another business, I am after something similar to this
Thanks

I have updated the design brief.
this should help make it easir and more clear
Thanks

Target Market(s)

Home owners from 30yrs +

Industry/Entity Type

Electrical

Requirements
Must have
• Logo - Not a main feature of card
1300 846 572 on both sides
Lic no: 418695D (doesn’t have to be big) prefer on back

The main feature of the front of the card is the 2 free movie tickets for Referee & $25 OFF Friends first bill

HOW ABOUT TWO FREE MOVIE TICKETS?
It is easy! Know someone who needs an electrician? Maybe a friend, family member, relative or work colleague.
Tell them about us, and we will take $25 off their first bill and give you two FREE Movie Tickets just for introducing us.
To make a referral fill out this card and give it to your friend.

Recommended By:____________
Address:__________________
Frinds name: _____________

*this offer is only valued for work over $55. Non transferable for cash. This coupon is limited to 1 per customer, not to be used in conjunction with any other offer
Nice to have
• Catchy heading on card
example- tell a friend for cash card, (if i was giving away cash vouchers..)

example- keep me in your wallet and pass me on

```html
<!DOCTYPE html>
<html lang="en">
<head>
<meta charset="utf-8">
<title>Referral Card – Back</title>
<link rel="stylesheet" href="https://fonts.googleapis.com/css2?family=Exo+2:wght@300&family=Great+Vibes&display=swap">
<style>
  :root {
    --red-bright: #ec1c24;
    --red-mid: #cf1c23;
    --red-deep: #a11a1f;
    --star-glow: rgba(230, 40, 50, 0.55);
    --ink: #141010;
    --paper: #ffffff;
  }
  * { margin: 0; padding: 0; box-sizing: border-box; }
  html, body {
    width: 1200px;
    height: 700px;
    overflow: hidden;
    background: var(--red-deep);
  }
  .card {
    position: relative;
    width: 1200px;
    height: 700px;
    overflow: hidden;
    background: linear-gradient(40deg, var(--red-bright) 0%, var(--red-mid) 45%, var(--red-deep) 100%);
    font-family: "Exo 2", "Trebuchet MS", sans-serif;
    font-weight: 300;
  }
  .card__decoration {
    position: absolute;
    left: 380px;
    top: 30px;
    width: 780px;
    height: 640px;
    background: radial-gradient(ellipse at 55% 50%, var(--star-glow) 0%, rgba(230, 40, 50, 0) 65%);
  }
  .contact {
    position: absolute;
    left: 46px;
    top: 94px;
    color: var(--ink);
    font-size: 34px;
    line-height: 44px;
    letter-spacing: -0.3px;
  }
  .form-row {
    position: absolute;
    left: 46px;
    width: 1100px;
    display: flex;
    align-items: flex-end;
  }
  .form-row--first { top: 292px; }
  .form-row--second { top: 464px; }
  .field {
    display: flex;
    align-items: flex-end;
  }
  .field--name { width: 528px; }
  .field--address { margin-left: 23px; width: 549px; }
  .field__label {
    font-family: "Great Vibes", "Brush Script MT", cursive;
    font-size: 56px;
    line-height: 64px;
    color: var(--ink);
    text-shadow: 0 2px 4px rgba(0, 0, 0, 0.45);
    white-space: nowrap;
  }
  .field__line {
    flex: 1;
    height: 1px;
    margin-left: 8px;
    margin-bottom: 10px;
    background: var(--ink);
  }
  .terms {
    position: absolute;
    left: 0;
    top: 580px;
    width: 1200px;
    text-align: center;
    color: var(--paper);
    font-size: 22.5px;
    line-height: 33px;
  }
</style>
</head>
<body>
  <main class="card">
    <div class="card__decoration" role="img" aria-label="Large faint outlined stars decorating the background"></div>

    <div class="contact">
      <p class="contact__phone">Phone number: 1300 846 572</p>
      <p class="contact__licence">Lic no: 418695D</p>
    </div>

    <div class="form-row form-row--first">
      <div class="field field--name">
        <span class="field__label">Name</span>
        <span class="field__line"></span>
      </div>
      <div class="field field--address">
        <span class="field__label">Address</span>
        <span class="field__line"></span>
      </div>
    </div>

    <div class="form-row form-row--second">
      <div class="field field--name">
        <span class="field__label">Name</span>
        <span class="field__line"></span>
      </div>
      <div class="field field--address">
        <span class="field__label">Address</span>
        <span class="field__line"></span>
      </div>
    </div>

    <p class="terms">*this offer is only valued for work over $55. Non transferable for cash. This coupon is<br>limited to 1 per customer, not to be used in conjunction with any other offer</p>
  </main>
</body>
</html>
```